High End Personalized Functional Medicine in Women's Health

We are adding new and exciting personalized medicine services to our Women's Health Care practice focusing on health optimization and anti-aging as well as hormone replacement therapy and need a high end brochure to educate patients about these services. We would like to see a zen-like design that has feminine appeal. Our office colors are vibrant but soothing. We have utilized the concepts of feng shui to optimize our positive energy. The exterior of the building is peach and cream and these colors would blend with that energy The final design should communicate a sense that you can take control of your health and aging.

Target Market(s)

Females age 35-65 with annual income >$75000/year

Industry/Entity Type

Health And Wellness

Logo Text

Bright Path is the company name. Our sister company is Corva Ridge Ob/Gyn

Font styles to use
Serif

Colors

Designer to choose colors to be used in the design.

Requirements
Must have
• My project must have clean lines. I like a strong feminine appearance, not a fluffy curvy feminine look. Professional appearance, Brochure would be on thicker card stock. A strong front page that makes you want to open the brochure
Nice to have
• Eye catching photos that complement our message . I am not tied to the peach and cream color recommendation, but find those colors feminine but not so cliche as pinks and purples.
Should not have
• frilly design

```html
<!DOCTYPE html>
<html lang="en">
<head>
<meta charset="utf-8">
<title>Bright Path Functional Medicine Brochure</title>
<link href="https://fonts.googleapis.com/css2?family=Pacifico&family=Raleway:wght@500;600;700&family=Roboto:wght@400;500;700&display=swap" rel="stylesheet">
<style>
:root{
  --backdrop:#464646;
  --paper:#ffffff;
  --brown:#a65f35;
  --brown-text:#9c5a32;
  --peach:#f6b690;
  --peach-soft:#f8c7a8;
  --olive:#d9d49e;
  --ink:#1c1c1c;
  --skin:#e9cfc1;
  --skin-deep:#d6ad98;
}
*{margin:0;padding:0;box-sizing:border-box}
html,body{width:1200px;height:1200px;overflow:hidden;background:var(--backdrop)}
body{position:relative;font-family:"Roboto",Arial,sans-serif;color:var(--ink)}
.page{position:absolute;top:204px;width:564px;height:790px;background:var(--paper);overflow:hidden}
.page--front{left:26px}
.page--inside{left:606px}
.art{position:absolute;left:0;top:0}
.script{font-family:"Pacifico",cursive;font-weight:400}
.front-title{position:absolute;left:17px;top:272px;font-size:29px;color:var(--brown);letter-spacing:-.5px;line-height:1.3}
.front-body{position:absolute;left:17px;top:322px;width:530px}
.lead{font-size:14.4px;line-height:16.5px;margin-bottom:7px}
.bio{font-size:10.8px;line-height:13.2px;text-align:justify}
.section-h{font-family:"Raleway",sans-serif;font-weight:600;color:var(--brown-text);font-size:13.8px;margin:16px 0 9px}
.testimonial{display:flex;gap:8px;align-items:flex-start}
.testimonial .mark{font-family:Georgia,serif;font-size:34px;line-height:28px;color:var(--brown);font-weight:700;width:22px;padding-left:4px}
.testimonial p{font-size:10.5px;line-height:13px;border-left:1.5px solid var(--peach);padding-left:9px}
.small{font-size:8.6px;line-height:11.2px;padding-left:2px}
.front-body .section-h.tight{margin:12px 0 7px}
.front-footer{position:absolute;left:0;right:0;top:752px;text-align:center;font-size:10px}
.inside-header{position:absolute;left:0;top:0;width:100%;height:52px;background:var(--brown);border-bottom:3px solid var(--peach);text-align:center}
.inside-header h1{font-size:28px;color:#fff;line-height:50px;letter-spacing:-.3px}
.symptoms{position:absolute;left:18px;top:56px;width:530px}
.symptom h2{font-family:"Raleway",sans-serif;font-weight:700;color:var(--brown-text);font-size:17.6px;line-height:22px;margin-bottom:3px}
.symptom p{font-size:8.8px;line-height:11.1px}
.symptom{margin-bottom:6px}
.url-pill{position:absolute;left:0;top:538px;height:19px;padding:0 8px 0 18px;background:var(--peach);border-radius:0 10px 10px 0;font-weight:700;font-size:11.5px;line-height:19px}
</style>
</head>
<body>

<section class="page page--front">
  <svg class="art" width="564" height="790" viewBox="0 0 564 790">
    <defs>
      <linearGradient id="portraitTone" x1="0" y1="0" x2="1" y2="0">
        <stop offset="0" stop-color="#e6c6b6"/>
        <stop offset=".5" stop-color="#e3c2b3"/>
        <stop offset=".85" stop-color="#d8c2b8"/>
        <stop offset="1" stop-color="#dcdde2"/>
      </linearGradient>
    </defs>
    <path d="M0 0H564V150C430 230 250 260 0 170Z" fill="url(#portraitTone)" role="img" aria-label="Photo of one woman's face shown at three stages of ageing"/>
    <path d="M0 115C110 220 330 250 564 150V166C330 270 110 250 0 178Z" fill="var(--olive)"/>
    <path d="M0 178C110 250 330 272 564 166V184C330 290 110 278 0 212Z" fill="#fff"/>
    <path d="M0 190C120 280 330 290 564 190V205C330 310 120 298 0 222Z" fill="var(--peach)"/>
    <circle cx="477" cy="220" r="76" fill="var(--peach)"/>
    <circle cx="477" cy="220" r="71" fill="#e8e2df" role="img" aria-label="Portrait of a woman with eyes closed touching her jawline"/>
    <path d="M0 712C160 665 380 670 564 705V790H0Z" fill="var(--olive)"/>
    <path d="M0 730C170 688 380 690 564 722V790H0Z" fill="#fff"/>
    <path d="M0 745C170 710 380 710 564 735V790H0Z" fill="var(--peach)"/>
  </svg>

  <h1 class="front-title script">Bright Path Functional Medicine</h1>

  <div class="front-body">
    <p class="lead">Functional medicine's aim is to heal the physical body in order to engage in our life purpose of connection and emotional and spiritual growth.</p>
    <p class="bio">Dr. Elena Varga specializes in women's health and has over 25 years of experience. She is an expert in bio-identical hormone replacement therapy and has been a Dermalis bio-identical hormone pellet practitioner for over 10 years. Dr. Varga has been practicing functional medicine for many years with a primary focus on hormone therapy, medical weight loss, and lifestyle change. She has recently expanded her practice to incorporate additional services including healing with a focus on adrenal, gastrointestinal and detoxification programs. Dr. Varga is a practitioner of the Harlow Method for functional medicine and works closely with Dr. Martin Harlow as her mentor in the development of individual treatment protocols for our patients. Dr. Harlow has over 25 years of experience in functional medicine.</p>

    <h2 class="section-h">What do patients' have to say about their experience with Dr. Varga</h2>
    <div class="testimonial">
      <span class="mark">&ldquo;</span>
      <p>Lorem ipsum is placeholder text commonly used in the graphic, print, and publishing industries for previewing layouts and visual mockups.</p>
    </div>

    <h2 class="section-h tight">Why should you consider a functional medicine visit?</h2>
    <p class="small">You are tired of feeling tired. You can't even focus on the future because you are so overwhelmed. The pain of being unable to think clearly and being too tired to exercise are your daily reality. Your life goals seem like too much to think about, you just have to get through today.</p>

    <h2 class="section-h tight">Who else should consider a functional medicine visit?</h2>
    <p class="small">You want to achieve OPTIMAL health with a personalized medicine approach. You are eating well, exercising and engaging in stress reducing activities such as meditation. You want to know how to minimize the effects of aging and are ready to take a proactive approach in getting to the highest level of health you can achieve.</p>
  </div>

  <p class="front-footer">For moe details please visit our website www.brightpathhealth.com</p>
</section>

<section class="page page--inside">
  <header class="inside-header"><h1 class="script">What Symptoms Do We Treat?</h1></header>

  <div class="symptoms">
    <article class="symptom">
      <h2>Weight Gain</h2>
      <p>Adrenal dysfunction results in cortisol imbalance. The major function of cortisol is to help balance blood sugar. When cortisol is out of balance, your body will store body fat rather than burning fat for fuel resulting in weight gain. Menopausal hormone imbalance will also result in abdominal weight gain.</p>
    </article>
    <article class="symptom">
      <h2>Fatigue</h2>
      <p>Adrenal exhaustion results from long term stress that depletes cortisol. Testing and correcting cortisol will improve energy levels. Long term stress can result in mitochondrial dysfunction and organic acid tests can tell us how to support your mitochondria.</p>
    </article>
    <article class="symptom">
      <h2>Depression</h2>
      <p>We focus both on cortisoland the brain neurotransmitters dopamine, epinephrine and norepinephrine to evaluate causes of depression. Hormone imbalance can also result in both anxiety and depression.</p>
    </article>
    <article class="symptom">
      <h2>Female Hormone Imbalance</h2>
      <p>Optimizing hormonal balance is our specialty. We focus on optimizing hormone levels with bio-identical hormones, but also know that adrenal treatment protocols can improve symptoms of hot flashes, nights sweats, and foggy thinking.</p>
    </article>
    <article class="symptom">
      <h2>GI problems</h2>
      <p>The immune cells that line our digestive tract are regulated by cortisol. Cortisol imbalance results in inflammation and "leaky gut" causing digestive symptoms like bloating, heartburn, constipation, or diarrhea. Utilizing a comprehensive program that includes avoiding inflammatory foods and GI Panel stool testing allow us to find underlying infections or sources of inflammation and allow us to develop a focused treatment plan.</p>
    </article>
    <article class="symptom">
      <h2>What can I expect from my first visit?</h2>
      <p>During your initial consultation, we want to get to know each other and find out your expectations for health. We will explore your health history and symptoms as well as lifestyle factors including diet and sleep. We will discuss your goals and reasons for getting healthy. We know that we must incorporate lifestyle changes including stress reduction, diet and exercise optimization in any program for healing. We will discuss testing recommendations including blood work, hormone evaluation, cortisol, GI, and organic acid tests as well as nutritional and personal coaching options.</p>
    </article>
    <article class="symptom">
      <h2>What are your treatment protocols based on?</h2>
      <p>Treatment protocols are based on making you feel better with a focused wellness program that treats underlying cause. We want to optimize body systems by reducing inflammation, treating insulin resistance, improving catabolic physiology, and reducing oxidative stress. Treatment protocols are a combination of supplement support and hormone balance in addition to lifestyle optimization. Supplement programs tend to be focused and last approximately 6 months. Hormone programs continue for as long as you have symptoms. We will work together to determine what type of treatment program works best for you.</p>
    </article>
  </div>

  <p class="url-pill">www.brightpathhealth.com</p>

  <svg class="art" width="564" height="790" viewBox="0 0 564 790" style="pointer-events:none">
    <defs>
      <linearGradient id="familyTone" x1="0" y1="0" x2="0" y2="1">
        <stop offset="0" stop-color="#9a8a6a"/>
        <stop offset=".55" stop-color="#8a7f70"/>
        <stop offset="1" stop-color="#6f8a46"/>
      </linearGradient>
    </defs>
    <path d="M0 620C150 570 380 545 564 560V790H0Z" fill="url(#familyTone)" role="img" aria-label="Photo of a smiling family of four seated on grass outdoors"/>
    <path d="M0 598C150 560 370 535 564 545V572C380 560 150 580 0 628Z" fill="var(--olive)"/>
    <path d="M0 615C150 580 380 558 564 568V580C380 570 150 592 0 632Z" fill="#fff"/>
  </svg>
</section>

</body>
</html>
```